Our companies name is The Gilded Ladle and we specialize in craft cupcakes, what I mean by that is that we bake our cupcakes with craft beer and other alcoholic drinks. We are trying to focus on being elegant but at the same time unpretentious. Since we are incorporating beer in our cupcakes we want the business card to have our logo in the front and our information in the back.

Once we select the best design we will provide the contact information to be added. Thank you.

Industry/Entity Type

Business

Font styles to use
Decorative
Script

Requirements
Must have
• Round corners
Should not have
• Square corners

```html
<!DOCTYPE html>
<html lang="en">
<head>
<meta charset="utf-8">
<title>The Gilded Ladle – Business Card</title>
<link rel="stylesheet" href="https://fonts.googleapis.com/css2?family=Great+Vibes&family=Josefin+Sans:wght@400;700&family=PT+Sans&display=swap">
<style>
  :root {
    --page-bg: #2b1517;
    --label-bar: #141414;
    --label-text: #8fc4bd;
    --card-white: #ffffff;
    --teal: #8fc4bd;
    --ink: #1c1c1c;
    --band-black: #1b1b1b;
    --accent-red: #e23a3f;
    --soft-white: #f2f2f2;
  }
  * { box-sizing: border-box; margin: 0; padding: 0; }
  html, body { width: 833px; height: 1200px; overflow: hidden; }
  body {
    position: relative;
    background: var(--page-bg);
    font-family: "Josefin Sans", sans-serif;
  }

  .card {
    position: absolute;
    left: 106px;
    width: 620px;
    height: 354px;
    border-radius: 18px;
    overflow: hidden;
    background: var(--card-white);
  }
  .card--back { top: 150px; }
  .card--front { top: 745px; }

  .side-label {
    position: absolute;
    left: 0;
    width: 833px;
    height: 42px;
    background: var(--label-bar);
    color: var(--label-text);
    font-family: "PT Sans", sans-serif;
    font-size: 31px;
    line-height: 42px;
    text-align: center;
  }
  .side-label--back { top: 573px; }
  .side-label--front { top: 1158px; }

  /* Back side */
  .back__top-band {
    position: absolute; top: 0; left: 0; right: 0;
    height: 16px; background: var(--teal);
  }
  .back__bottom-band {
    position: absolute; bottom: 0; left: 0; right: 0;
    height: 84px; background: var(--band-black);
    display: flex; align-items: center; justify-content: space-around;
    padding: 0 20px;
  }
  .brand {
    display: flex; align-items: center; gap: 12px;
  }
  .brand__dot {
    width: 22px; height: 22px; border-radius: 50%;
    background: var(--accent-red);
  }
  .brand__name {
    font-family: "Josefin Sans", sans-serif;
    font-weight: 700;
    color: var(--ink);
    text-transform: uppercase;
    letter-spacing: 1px;
  }
  .back__brand {
    position: absolute; left: 48px; top: 114px;
  }
  .back__brand .brand__name { font-size: 24px; }

  .person {
    position: absolute; right: 52px; top: 70px; text-align: center;
  }
  .person__name {
    font-family: "Great Vibes", cursive;
    font-size: 52px; color: var(--ink); line-height: 1;
  }
  .person__role {
    font-size: 14px; letter-spacing: 3px; color: var(--ink);
    text-transform: uppercase; margin-top: 2px;
  }

  .contact {
    display: flex; align-items: center; gap: 12px;
    color: var(--soft-white); font-size: 14px; letter-spacing: .5px;
  }
  .contact__icon {
    width: 34px; height: 34px; border-radius: 50%;
    background: var(--card-white);
    display: flex; align-items: center; justify-content: center;
  }
  .contact__icon svg { width: 18px; height: 18px; }

  /* Front side */
  .card--front { background: var(--teal); }
  .front__panel {
    position: absolute; inset: 22px;
    background: var(--card-white);
    border: 3px solid var(--accent-red);
    border-radius: 10px;
    display: flex; align-items: center; justify-content: center;
  }
  .front__panel .brand__name { font-size: 34px; }
  .front__panel .brand__dot { width: 30px; height: 30px; }
</style>
</head>
<body>

  <section class="card card--back" aria-label="Business card back side">
    <div class="back__top-band"></div>

    <div class="brand back__brand">
      <span class="brand__dot"></span>
      <span class="brand__name">The Gilded Ladle</span>
    </div>

    <div class="person">
      <p class="person__name">Mara Quill</p>
      <p class="person__role">Owner</p>
    </div>

    <div class="back__bottom-band">
      <div class="contact">
        <span class="contact__icon">
          <svg viewBox="0 0 24 24" aria-hidden="true"><rect x="6.5" y="2" width="11" height="20" rx="2" fill="none" stroke="#1b1b1b" stroke-width="2"/><circle cx="12" cy="18.5" r="1.2" fill="#1b1b1b"/></svg>
        </span>
        <span class="contact__text">+1 555 0142 318</span>
      </div>
      <div class="contact">
        <span class="contact__icon">
          <svg viewBox="0 0 24 24" aria-hidden="true"><path d="M6.6 10.8a15 15 0 0 0 6.6 6.6l2.2-2.2a1 1 0 0 1 1-.25 11.4 11.4 0 0 0 3.6.57 1 1 0 0 1 1 1V20a1 1 0 0 1-1 1A17 17 0 0 1 3 4a1 1 0 0 1 1-1h3.5a1 1 0 0 1 1 1c0 1.25.2 2.45.57 3.57a1 1 0 0 1-.25 1z" fill="#1b1b1b"/></svg>
        </span>
        <span class="contact__text">+1 555 0142 318</span>
      </div>
      <div class="contact">
        <span class="contact__icon">
          <svg viewBox="0 0 24 24" aria-hidden="true"><rect x="3" y="6" width="18" height="12" rx="1.5" fill="#1b1b1b"/><path d="M3.5 6.8 12 13l8.5-6.2" fill="none" stroke="#fff" stroke-width="1.6"/></svg>
        </span>
        <span class="contact__text">mara@gildedladle.com</span>
      </div>
    </div>
  </section>

  <div class="side-label side-label--back">Back-Side</div>

  <section class="card card--front" aria-label="Business card front side">
    <div class="front__panel">
      <div class="brand">
        <span class="brand__dot"></span>
        <span class="brand__name">The Gilded Ladle</span>
      </div>
    </div>
  </section>

  <div class="side-label side-label--front">Front-Side</div>

</body>
</html>
```